i am creating an a new cold brew coffee and need a standard format for 5 different flavours. the PDF with 5 colours is what i created as a format and the one page PDF is the style i like but am happy yo move away from it.. the images are the style i like

i am looking for a nice clean tidy but standard out label that will pop off a brown paper backing.

Target Market(s)

18-40 Yr old coffee lovers wanting a high end cold brew coffee

Font styles to use
Serif
Sans Serif

Colors

Designer to choose colors to be used in the design.

Requirements
Must have
• i want a standard format that a component can change colour with flavours, brown paper background. i need the nutritional content box at the back ( as per PDF ) and i would like the text added also, as this is a description of the product
Nice to have
• i like the tidy clinical look of the font pharma bold condensed
• the PDF's show the flavours.. the one with a brown background is something i have seen that i like and the images are the styles i like .

```html
<!DOCTYPE html>
<html lang="en">
<head>
<meta charset="utf-8">
<title>Harbour Brews – Sparkling Ginger Cold Brew Label</title>
<link href="https://fonts.googleapis.com/css2?family=Montserrat:wght@800&family=Kaushan+Script&family=Roboto+Condensed:wght@700&family=Playfair+Display:ital@1&display=swap" rel="stylesheet">
<style>
  :root {
    --kraft: #c7a47d;
    --kraft-dark: #b38f67;
    --flavour-red: #f0361b;
    --paper-white: #ffffff;
    --ink: #1c1a19;
    --bean-dark: #5a3a22;
    --bean-light: #8a6040;
    --seal-blue: #2f3d8f;
  }
  * { margin: 0; padding: 0; box-sizing: border-box; }
  html, body {
    width: 1200px; height: 568px; overflow: hidden;
    background: var(--paper-white);
  }
  .label {
    position: relative;
    width: 1200px; height: 568px;
    overflow: hidden;
    background: radial-gradient(ellipse at 60% 40%, var(--kraft) 0%, var(--kraft-dark) 100%);
  }
  .rule { position: absolute; }
  .rule--white { background: var(--paper-white); }
  .rule--red { background: var(--flavour-red); }

  .flavour-band {
    position: absolute;
    left: 30px; top: 362px;
    width: 1144px; height: 98px;
    background: var(--flavour-red);
  }
  .category-word {
    position: absolute;
    left: 282px; top: 284px;
    transform: translate(-50%, -50%) rotate(-90deg);
    font-family: "Roboto Condensed", "Arial Narrow", sans-serif;
    font-weight: 700;
    font-size: 168px;
    line-height: 1;
    letter-spacing: 2px;
    color: var(--flavour-red);
    -webkit-text-stroke: 4px var(--paper-white);
    paint-order: stroke fill;
    white-space: nowrap;
  }
  .brand-name {
    position: absolute;
    left: 412px; top: 104px;
    width: 420px;
    font-family: "Montserrat", sans-serif;
    font-weight: 800;
    font-size: 68px;
    line-height: 84px;
    letter-spacing: 2px;
    color: var(--ink);
    white-space: nowrap;
  }
  .origin-seal {
    position: absolute;
    left: 870px; top: 40px;
    width: 264px; height: 264px;
  }
  .flavour-name {
    position: absolute;
    left: 420px; top: 366px;
    width: 620px;
    text-align: center;
    font-family: "Kaushan Script", cursive;
    font-size: 66px;
    line-height: 88px;
    color: var(--paper-white);
  }
  .volume-badge {
    position: absolute;
    left: 1072px; top: 376px;
    width: 76px; height: 76px;
    border: 3px solid var(--ink);
    border-radius: 50%;
    display: flex; align-items: center; justify-content: center;
    font-family: "Playfair Display", serif;
    font-style: italic;
    font-size: 17px;
    color: var(--ink);
  }
  .bean-strip {
    position: absolute;
    left: 402px; top: 470px;
    width: 772px; height: 86px;
    border-radius: 40px;
    background: linear-gradient(90deg, var(--bean-light), var(--bean-dark) 50%, var(--bean-light));
    opacity: 0.85;
  }
</style>
</head>
<body>
<main class="label">
  <div class="rule rule--white" style="left:30px; top:28px; width:296px; height:7px;"></div>
  <div class="rule rule--white" style="left:372px; top:28px; width:802px; height:7px;"></div>
  <div class="rule rule--white" style="left:136px; top:28px; width:28px; height:510px;"></div>
  <div class="rule rule--white" style="left:180px; top:28px; width:14px; height:510px;"></div>
  <div class="rule rule--white" style="left:30px; top:460px; width:1144px; height:9px;"></div>
  <div class="rule rule--white" style="left:30px; top:500px; width:330px; height:6px;"></div>
  <div class="rule rule--white" style="left:348px; top:26px; width:10px; height:512px;"></div>
  <div class="rule rule--red" style="left:362px; top:26px; width:10px; height:512px;"></div>
  <div class="rule rule--red" style="left:372px; top:480px; width:802px; height:12px;"></div>

  <div class="flavour-band"></div>

  <div class="category-word">Coffee</div>

  <div class="brand-name">HARBOUR<br>BREWS</div>

  <svg class="origin-seal" viewBox="0 0 274 274" aria-hidden="true">
    <circle cx="137" cy="137" r="134" fill="#ffffff"/>
    <circle cx="137" cy="137" r="124" fill="#f0361b"/>
    <circle cx="137" cy="137" r="110" fill="#ffffff"/>
    <circle cx="137" cy="137" r="98" fill="#2f3d8f"/>
    <circle cx="137" cy="137" r="66" fill="#ffffff"/>
  </svg>

  <div class="flavour-name">Sparkling Ginger</div>
  <div class="volume-badge">330 ml</div>

  <div class="bean-strip" role="img" aria-label="Row of roasted coffee beans"></div>
</main>
</body>
</html>
```